Maple. Step PT Tri-Fold

An on demand house call mobile physical therapy and wellness company. Focused on quality rehabilitation management health and wellness needs to your door.
We need a tri-fold brochure to describe our services

Target Market(s)

Patients in need of physical therapy

Industry/Entity Type

Physical Therapy

Font styles to use
Serif
Sans Serif
Other font styles liked:
• Attached is some necessary content from a prior brochure

Colors
0054AA
0677BA
7BADD7
CADEEF
E8F1F8
EB3D1F
EC4F4E
F09395
F8D3D4
FCEDEE

```html
<!DOCTYPE html>
<html lang="en">
<head>
<meta charset="utf-8">
<title>Maple. Step PT – Tri-Fold Brochure</title>
<link rel="stylesheet" href="https://fonts.googleapis.com/css2?family=Arimo:wght@400&family=Poppins:wght@400;500;600;800&display=swap">
<style>
  :root{
    --backdrop:#6f6f6d;
    --label:#2e2e2e;
    --red:#d8393f;
    --red-deep:#c92f36;
    --red-soft:#e9686c;
    --pink:#f09395;
    --blush:#f8d3d4;
    --ice:#e8f1f8;
    --blue:#0677ba;
    --ink:#222222;
    --white:#ffffff;
  }
  *{box-sizing:border-box;margin:0;padding:0}
  html,body{width:824px;height:1200px;overflow:hidden;background:var(--backdrop)}
  .stage{position:absolute;left:0;top:0;width:1596px;height:2323px;transform:scale(.51629);transform-origin:0 0;background:var(--backdrop);font-family:"Poppins",sans-serif}
  .side-label{position:absolute;left:0;width:1596px;text-align:center;font-family:"Arimo",sans-serif;font-size:40px;color:var(--label);letter-spacing:1px}
  .side-label.front{top:84px}
  .side-label.inside{top:1188px}
  .sheet{position:absolute;left:154px;width:1288px;height:988px;overflow:hidden;background:var(--white)}
  .sheet.front{top:160px}
  .sheet.inside{top:1252px}
  .sheet svg.shapes{position:absolute;left:0;top:0;width:1288px;height:988px}
  .abs{position:absolute}

  /* front – insurance panel */
  .insurance-title{left:38px;top:62px;font-size:40px;line-height:46px;font-weight:800;color:var(--white);letter-spacing:.5px}
  .insurance-note{left:37px;top:175px;font-size:23px;line-height:33px;color:var(--white)}
  .partner-badge{position:absolute;background:var(--white)}

  /* brand lockups */
  .brand{position:absolute;display:flex;align-items:center}
  .brand-dot{border-radius:50%;border:6px solid var(--red);flex:none}
  .brand-name{color:var(--blue);font-weight:600;white-space:nowrap}

  .cover-brand{left:420px;top:620px;width:434px;flex-direction:column}
  .cover-brand .brand-dot{width:90px;height:90px}
  .cover-brand .brand-name{font-size:42px;margin-top:18px}

  .contact-list{left:520px;top:826px;list-style:none}
  .contact-list li{display:flex;align-items:center;height:34px;font-size:23px;color:var(--ink)}
  .contact-badge{width:20px;height:20px;border-radius:50%;background:var(--red);color:var(--white);font-size:11px;font-weight:600;display:flex;align-items:center;justify-content:center;margin-right:20px;flex:none}

  .tagline{left:938px;top:670px;font-size:32px;line-height:36px;font-weight:800;color:var(--ink)}
  .tagline-copy{left:938px;top:746px;font-size:21px;line-height:26.5px;color:var(--ink)}
  .back-brand{left:938px;top:878px}
  .back-brand .brand-dot{width:64px;height:64px;border-width:5px}
  .back-brand .brand-name{font-size:30px;margin-left:20px}

  /* inside */
  .tab-brand{left:46px;top:36px}
  .tab-brand .brand-dot{width:42px;height:42px;border-width:4px}
  .tab-brand .brand-name{font-size:21px;margin-left:10px}
  .intro{left:51px;top:118px;font-size:23.5px;line-height:41px;color:var(--red);white-space:nowrap;letter-spacing:-.2px}
  .intro strong{font-weight:800}
  .benefits{left:446px;top:80px;width:382px;list-style:none}
  .benefits li{position:absolute;left:0;width:382px;padding-left:48px;font-size:16px;line-height:26.5px;letter-spacing:-.45px;color:var(--ink);text-align:justify}
  .benefits svg{position:absolute;left:0;top:6px;width:32px;height:28px}
  .programs-title{left:856px;top:468px;width:432px;text-align:center;font-size:34px;line-height:42px;font-weight:800;color:var(--white);letter-spacing:.5px}
  .program{position:absolute;width:150px;text-align:center;font-size:15.5px;color:var(--white)}
  .program-mark{position:absolute;width:80px;height:80px;border-radius:50%;border:3px solid var(--white);background:var(--red-soft)}
  .program-feature{left:1140px;top:878px;font-size:19px;line-height:22px;font-weight:800;color:var(--white)}
</style>
</head>
<body>
<main class="stage">

  <p class="side-label front">FRONT</p>

  <section class="sheet front" aria-label="Brochure outside">
    <svg class="shapes" viewBox="0 0 1288 988">
      <defs>
        <linearGradient id="coverRed" x1="0" y1="0" x2="1" y2="1">
          <stop offset="0" stop-color="#d8393f"/><stop offset=".7" stop-color="#e2575b"/><stop offset="1" stop-color="#ee8d90"/>
        </linearGradient>
        <linearGradient id="rightRed" x1="1" y1="0" x2="0" y2="1">
          <stop offset="0" stop-color="#d8393f"/><stop offset="1" stop-color="#ee8486"/>
        </linearGradient>
        <linearGradient id="stretchPhoto" x1="0" y1="0" x2="1" y2="1">
          <stop offset="0" stop-color="#e9ecee"/><stop offset=".5" stop-color="#c9ced6"/><stop offset="1" stop-color="#eef0f2"/>
        </linearGradient>
        <linearGradient id="handsPhoto" x1="0" y1="0" x2="1" y2="1">
          <stop offset="0" stop-color="#c8d3d6"/><stop offset=".5" stop-color="#e6d4c8"/><stop offset="1" stop-color="#f1f3f4"/>
        </linearGradient>
        <linearGradient id="foldShade" x1="0" y1="0" x2="1" y2="0">
          <stop offset="0" stop-color="#000" stop-opacity="0"/><stop offset=".5" stop-color="#000" stop-opacity=".12"/><stop offset="1" stop-color="#000" stop-opacity="0"/>
        </linearGradient>
      </defs>

      <rect x="0" y="0" width="420" height="608" fill="var(--red)"/>
      <path d="M150 0 Q360 40 420 230 L420 0 Z" fill="var(--pink)"/>
      <path d="M150 0 Q360 40 420 230" fill="none" stroke="var(--white)" stroke-width="4"/>
      <rect x="0" y="608" width="420" height="380" fill="url(#handsPhoto)" role="img" aria-label="Photo of a clinician gently holding a patient's hands across a desk"/>

      <rect x="420" y="0" width="868" height="760" fill="url(#stretchPhoto)" role="img" aria-label="Photo of a therapist stretching a woman's leg on a living-room floor"/>
      <polygon points="420,70 900,650 903,700 420,140" fill="var(--ice)"/>
      <polygon points="420,140 903,700 856,752 420,752" fill="url(#coverRed)"/>
      <path d="M420 745 L622 522 Q636 506 650 522 L854 745 L854 988 L420 988 Z" fill="var(--white)"/>
      <polygon points="856,750 896,665 1288,150 1288,988 856,988" fill="var(--ice)"/>
      <path d="M1288 160 L1288 612 L1058 562 Q1040 556 1050 542 Z" fill="url(#rightRed)"/>
      <polygon points="1046,988 1288,800 1288,988" fill="var(--white)"/>

      <rect x="405" y="0" width="30" height="988" fill="url(#foldShade)"/>
      <rect x="839" y="0" width="30" height="988" fill="url(#foldShade)"/>
    </svg>

    <h2 class="abs insurance-title">ACCEPTED<br>INSURANCES:</h2>
    <p class="abs insurance-note">Incudes all ADVANTAGE,<br>LTC, and CareState plans:</p>

    <div class="partner-badge" style="left:37px;top:280px;width:123px;height:47px"></div>
    <div class="partner-badge" style="left:169px;top:280px;width:97px;height:47px"></div>
    <div class="partner-badge" style="left:275px;top:280px;width:97px;height:47px"></div>
    <div class="partner-badge" style="left:37px;top:343px;width:123px;height:47px"></div>
    <div class="partner-badge" style="left:169px;top:343px;width:122px;height:47px"></div>
    <div class="partner-badge" style="left:299px;top:343px;width:85px;height:47px"></div>
    <div class="partner-badge" style="left:37px;top:407px;width:123px;height:47px"></div>
    <div class="partner-badge" style="left:169px;top:407px;width:122px;height:47px"></div>
    <div class="partner-badge" style="left:300px;top:407px;width:66px;height:87px"></div>
    <div class="partner-badge" style="left:37px;top:468px;width:86px;height:48px"></div>
    <div class="partner-badge" style="left:132px;top:468px;width:142px;height:48px"></div>
    <div class="partner-badge" style="left:37px;top:534px;width:123px;height:47px"></div>
    <div class="partner-badge" style="left:169px;top:534px;width:101px;height:47px"></div>

    <div class="brand cover-brand">
      <span class="brand-dot"></span>
      <span class="brand-name">Maple. Step PT</span>
    </div>

    <ul class="abs contact-list">
      <li><span class="contact-badge">P</span>(555) 214-7780</li>
      <li><span class="contact-badge">F</span>(555) 214-7781</li>
      <li><span class="contact-badge">E</span>hello@maplesteppt.com</li>
      <li><span class="contact-badge">W</span>www.maplesteppt.com</li>
    </ul>

    <h1 class="abs tagline">PHYSICAL THERAPY,<br>DELIVERED TO YOU</h1>
    <p class="abs tagline-copy">Finding the right rehabilitation<br>setting shapes recovery<br>Convenient support and<br>expert therapist</p>
    <div class="brand back-brand">
      <span class="brand-dot"></span>
      <span class="brand-name">Maple. Step PT</span>
    </div>
  </section>

  <p class="side-label inside">INSIDE</p>

  <section class="sheet inside" aria-label="Brochure inside">
    <svg class="shapes" viewBox="0 0 1288 988">
      <defs>
        <linearGradient id="exercisePhoto" x1="0" y1="0" x2="1" y2="1">
          <stop offset="0" stop-color="#9aa3a8"/><stop offset=".45" stop-color="#c8b7a5"/><stop offset="1" stop-color="#dad6cf"/>
        </linearGradient>
        <linearGradient id="clinicPhoto" x1="0" y1="0" x2="1" y2="1">
          <stop offset="0" stop-color="#cfdce6"/><stop offset=".6" stop-color="#a9bccb"/><stop offset="1" stop-color="#e4eaef"/>
        </linearGradient>
        <linearGradient id="programsRed" x1="0" y1="0" x2="0" y2="1">
          <stop offset="0" stop-color="#d8393f"/><stop offset="1" stop-color="#ec6f72"/>
        </linearGradient>
        <linearGradient id="foldShadeIn" x1="0" y1="0" x2="1" y2="0">
          <stop offset="0" stop-color="#000" stop-opacity="0"/><stop offset=".5" stop-color="#000" stop-opacity=".12"/><stop offset="1" stop-color="#000" stop-opacity="0"/>
        </linearGradient>
      </defs>

      <rect x="0" y="0" width="856" height="30" fill="var(--red)"/>
      <rect x="0" y="42" width="40" height="8" fill="var(--red)"/>
      <rect x="360" y="44" width="496" height="14" rx="7" fill="var(--pink)"/>
      <rect x="30" y="22" width="226" height="60" fill="var(--white)"/>

      <path d="M0 600 C80 530 160 478 216 468 C400 520 620 660 851 643 L851 662 C620 690 400 600 226 540 C140 548 70 592 0 640 Z" fill="var(--red)"/>
      <path d="M3 638 C80 588 160 548 226 540 C400 600 620 690 851 658 L851 985 L3 985 Z" fill="url(#exercisePhoto)" role="img" aria-label="Photo of a therapist guiding an older man lifting dumbbells at home"/>

      <rect x="856" y="0" width="432" height="448" fill="var(--pink)"/>
      <path d="M856 200 C950 80 1100 20 1288 10" fill="none" stroke="var(--white)" stroke-width="18"/>
      <path d="M856 222 C950 100 1100 42 1288 32" fill="none" stroke="var(--red)" stroke-width="14"/>
      <path d="M856 240 C950 122 1100 62 1288 54 L1288 448 L856 448 Z" fill="url(#clinicPhoto)" role="img" aria-label="Photo of a nurse talking with an older woman in a wheelchair in a clinic"/>
      <rect x="856" y="448" width="432" height="540" fill="url(#programsRed)"/>

      <rect x="419" y="0" width="30" height="988" fill="url(#foldShadeIn)"/>
      <rect x="841" y="0" width="30" height="988" fill="url(#foldShadeIn)"/>
    </svg>

    <div class="brand tab-brand">
      <span class="brand-dot"></span>
      <span class="brand-name">Maple. Step PT</span>
    </div>

    <p class="abs intro"><strong>OUR HOME-BASED</strong> outpatient<br><strong>PHYSICAL THERAPY</strong> delivers<br>high quality therapy services<br>in the comfort of your own<br>home.<br>Patients are not required to<br>be “homebound,” as they<br>would in the home health<br>setting.</p>

    <ul class="abs benefits">
      <li style="top:4px"><svg viewBox="0 0 32 28"><path d="M2 14 L12 25 L30 2" fill="none" stroke="var(--red)" stroke-width="5" stroke-linecap="round" stroke-linejoin="round"/></svg>Not having to arrange for someone to drive them to a clinic</li>
      <li style="top:68px"><svg viewBox="0 0 32 28"><path d="M2 14 L12 25 L30 2" fill="none" stroke="var(--red)" stroke-width="5" stroke-linecap="round" stroke-linejoin="round"/></svg>The privacy that comes from one-on-one care</li>
      <li style="top:133px"><svg viewBox="0 0 32 28"><path d="M2 14 L12 25 L30 2" fill="none" stroke="var(--red)" stroke-width="5" stroke-linecap="round" stroke-linejoin="round"/></svg>Building a treatment plan around how they live</li>
      <li style="top:197px"><svg viewBox="0 0 32 28"><path d="M2 14 L12 25 L30 2" fill="none" stroke="var(--red)" stroke-width="5" stroke-linecap="round" stroke-linejoin="round"/></svg>The use of the home to provide space for exercise in order to build commitment to a home exercise plan</li>
      <li style="top:288px"><svg viewBox="0 0 32 28"><path d="M2 14 L12 25 L30 2" fill="none" stroke="var(--red)" stroke-width="5" stroke-linecap="round" stroke-linejoin="round"/></svg>The sense of independence gained from getting better and gaining function in the home</li>
      <li style="top:378px"><svg viewBox="0 0 32 28"><path d="M2 14 L12 25 L30 2" fill="none" stroke="var(--red)" stroke-width="5" stroke-linecap="round" stroke-linejoin="round"/></svg>The sense of family that comes from knowing you have a skilled clinician who knows the ins and outs of your home and your loved one's challenges and can be reached when you need them.</li>
    </ul>

    <h2 class="abs programs-title">REHABILITATION<br>PROGRAMS:</h2>

    <span class="program-mark" style="left:907px;top:573px"></span>
    <span class="program-mark" style="left:1043px;top:573px"></span>
    <span class="program-mark" style="left:1162px;top:573px"></span>
    <span class="program-mark" style="left:907px;top:706px"></span>
    <span class="program-mark" style="left:1043px;top:706px"></span>
    <span class="program-mark" style="left:1162px;top:706px"></span>
    <span class="program-mark" style="left:907px;top:841px"></span>
    <span class="program-mark" style="left:1043px;top:841px"></span>

    <p class="program" style="left:872px;top:666px">Geriatrics</p>
    <p class="program" style="left:1008px;top:666px">Neurological</p>
    <p class="program" style="left:1127px;top:666px">Orthopedics</p>
    <p class="program" style="left:872px;top:796px">Sports Medicine</p>
    <p class="program" style="left:1008px;top:796px">Post-Operative</p>
    <p class="program" style="left:1127px;top:798px">CHF</p>
    <p class="program" style="left:862px;top:931px;width:170px">Balance/Vestibular</p>
    <p class="program" style="left:1008px;top:931px">COPD</p>
    <p class="abs program-feature">Home safety<br>and fall<br>prevention</p>
  </section>

</main>
</body>
</html>
```